MARGOT LISELLE - brand producing beautiful ladies bags to go through the day in an organized way

We need for a brand in-creation a lifestyle luxury website (ie Renaud Castel, Halworth, LunaVeda) with an online shop. The brand name will be www.margotliselle.com. Ideally, we would like to host the web in WebNook. However, we need specific fonts - Didot (brand name) combined with Century Gothic (for the rest) or perhaps propose a better combination if you feel. The web should contain an e-shop. We would like to have a mobile version of the web too.

Target Market(s)

female customers aged 14 - 35

Industry/Entity Type

Fashion

Contact Information for Business Card

Margot Liselle Brandt - CEO; Margot.Brandt@margotliselle.com; +420 608 312957
Tomas Brandt; Tomas.Brandt@margotliselle.com; cell +420 607915426
www.Margotliselle.com

Coding

Coded - Design and coding required

Number of Pages Required

5+ page

Font styles to use
Other font styles liked:
• Didot & Century Gothic or similar

Colors

Designer to choose colors to be used in the design.

Requirements
Must have
• the top line bar - please take inspiration from Halworth (no white background). The background should be incorporated in the main image. The brand name will be home button in top left corner. The brand should have feel of lifestyle luxury but functionality - those should be the features of the products (bags). The bags are currently being designed. Functional e-shop - would like to ideally use webnook.com.
Nice to have
• Personal Information should be hidden.

```html
<!DOCTYPE html>
<html lang="en">
<head>
<meta charset="utf-8">
<title>Margot Liselle</title>
<link rel="stylesheet" href="https://fonts.googleapis.com/css2?family=Bodoni+Moda:wght@400;500&family=Jost:wght@400;500;600&display=swap">
<style>
:root{
  --ink:#111111;
  --text:#2a2a2a;
  --muted:#6f6f6f;
  --white:#ffffff;
  --tile:#f3f3f3;
  --sand:#c6a98d;
  --rule:#d8d8d8;
}
*{margin:0;padding:0;box-sizing:border-box}
html,body{width:1200px;height:4228px;overflow:hidden;background:var(--white)}
body{position:relative;font-family:"Jost",sans-serif;color:var(--text)}
a{text-decoration:none}
.abs{position:absolute}
.display{font-family:"Bodoni Moda",serif;font-weight:400;letter-spacing:2px;color:var(--ink)}
.photo{position:absolute;overflow:hidden}

/* hero */
.hero{left:0;top:0;width:1200px;height:772px;
  background:
    radial-gradient(ellipse 260px 420px at 690px 420px,rgba(236,224,214,.85),rgba(236,224,214,0) 70%),
    radial-gradient(ellipse 180px 120px at 620px 660px,rgba(236,200,206,.8),rgba(236,200,206,0) 75%),
    radial-gradient(ellipse 520px 520px at 1020px 260px,rgba(244,226,206,.9),rgba(244,226,206,0) 70%),
    linear-gradient(105deg,#8c6147 0%,#b88c6c 30%,#d7b597 55%,#e9d3bd 100%)}
.brand{left:110px;top:33px;font-size:27px;color:var(--ink);letter-spacing:2px}
.nav{left:440px;top:40px;font-size:14px;font-weight:500;color:var(--ink)}
.nav a{position:absolute;white-space:nowrap;color:var(--ink)}
.nav-icons{left:950px;top:38px}
.play{left:173px;top:375px;width:80px;height:80px;border-radius:50%;background:rgba(255,255,255,.4)}
.play span{position:absolute;left:11px;top:11px;width:58px;height:58px;border-radius:50%;background:var(--white)}

/* bags */
.section-title{font-size:37px;text-align:center}
.product{position:absolute;top:927px;width:177px}
.product .thumb{width:177px;height:232px;background:var(--tile);position:relative}
.product .thumb i{position:absolute;left:22px;top:62px;width:133px;height:108px;border-radius:14px 14px 10px 10px;box-shadow:0 10px 14px -8px rgba(0,0,0,.25)}
.product .name{position:absolute;top:242px;left:0;width:177px;text-align:center;font-size:16px;font-weight:500;color:var(--ink)}
.product .price{position:absolute;top:264px;left:0;width:177px;text-align:center;font-size:14px;color:var(--ink)}
.product svg{position:absolute;left:162px;top:245px}

.btn-dark{display:flex;align-items:center;justify-content:center;background:var(--ink);color:var(--white);font-size:15px;font-weight:600;letter-spacing:.5px}
.caption{font-size:21px;font-weight:500;color:var(--ink);text-align:center;width:560px;letter-spacing:.5px}

/* about */
.about{left:0;top:3447px;width:1200px;height:409px;background:var(--sand)}
.about h2{position:absolute;top:88px;width:1200px;text-align:center;font-size:36px;color:var(--white)}
.about p{position:absolute;top:150px;left:165px;width:870px;text-align:center;font-size:14.5px;line-height:28px;color:var(--white)}
.btn-light{left:519px;top:266px;width:161px;height:46px;background:var(--white);color:var(--ink);font-size:14px;font-weight:600;display:flex;align-items:center;justify-content:center}

/* footer */
.footer-mark{left:100px;top:4010px;font-family:"Bodoni Moda",serif;font-size:22px;line-height:30px;color:var(--ink);letter-spacing:2px}
.col-head{font-size:13px;font-weight:600;color:var(--ink);letter-spacing:.5px}
.col-links{list-style:none;font-size:12px;color:var(--muted);line-height:26.5px}
.newsletter-note{font-size:12px;color:var(--muted);line-height:18px;width:330px}
.email{left:703px;top:4033px;width:265px;height:45px;border:1px solid var(--rule);font-size:12px;color:var(--muted);padding:15px 18px}
.subscribe{left:977px;top:4033px;width:110px;height:45px;font-size:14px}
.social{top:4104px;width:36px;height:36px;border:1.5px solid var(--ink);border-radius:50%;display:flex;align-items:center;justify-content:center}
.rule{left:112px;top:4170px;width:975px;height:1px;background:var(--rule)}
.copyright{left:0;top:4193px;width:1200px;text-align:center;font-size:11px;color:var(--muted)}
</style>
</head>
<body>

<header>
  <div class="abs hero" role="img" aria-label="Woman in a floral top holding a pale pink handbag on a sunlit city street"></div>
  <a class="abs brand display" href="#">MARGOT LISELLE</a>
  <nav class="abs nav">
    <a style="left:0">ACCESSORIES</a>
    <a style="left:123px">BAGS</a>
    <a style="left:192px">ABOUT MARGOT LISELLE</a>
    <a style="left:400px">CONTACT</a>
  </nav>
  <svg class="abs nav-icons" width="150" height="24" viewBox="0 0 150 24" aria-label="Search, account, wishlist, cart">
    <g fill="none" stroke="#111" stroke-width="2.4"><circle cx="10" cy="10" r="5.5"/><line x1="14" y1="14" x2="19" y2="19"/></g>
    <circle cx="50" cy="8" r="4" fill="#111"/><path d="M43 19c0-5 3-7 7-7s7 2 7 7z" fill="#111"/>
    <path d="M87 19l-7-7a4 4 0 0 1 7-5a4 4 0 0 1 7 5z" fill="#111"/>
    <path d="M121 9h14l-1 11h-12z" fill="#111"/><path d="M124 9a4 4 0 0 1 8 0" fill="none" stroke="#111" stroke-width="2"/>
  </svg>
  <div class="abs play" aria-label="Play video"><span></span>
    <svg class="abs" style="left:33px;top:31px" width="18" height="18" viewBox="0 0 18 18"><path d="M3 1l13 8-13 8z" fill="#111"/></svg>
  </div>
</header>

<main>
  <section class="bags">
    <h2 class="abs section-title display" style="left:0;top:852px;width:1200px">BAGS</h2>
    <article class="product" style="left:62px"><div class="thumb"><i role="img" aria-label="Tan leather crossbody bag" style="background:linear-gradient(160deg,#d3a77c,#a8784f)"></i></div><p class="name">Product Tittle</p><p class="price">$50.00</p><svg width="16" height="15" viewBox="0 0 16 15"><path d="M8 13.5l-5.8-5.8a3.3 3.3 0 0 1 5.8-3.6a3.3 3.3 0 0 1 5.8 3.6z" fill="none" stroke="#111" stroke-width="1.3"/></svg></article>
    <article class="product" style="left:287px"><div class="thumb"><i role="img" aria-label="Orange saddle bag" style="background:linear-gradient(160deg,#f0913f,#c8601e);border-radius:50px 50px 12px 12px"></i></div><p class="name">Product Tittle</p><p class="price">$50.00</p><svg width="16" height="15" viewBox="0 0 16 15"><path d="M8 13.5l-5.8-5.8a3.3 3.3 0 0 1 5.8-3.6a3.3 3.3 0 0 1 5.8 3.6z" fill="none" stroke="#111" stroke-width="1.3"/></svg></article>
    <article class="product" style="left:512px"><div class="thumb"><i role="img" aria-label="Cream top-handle bag" style="background:linear-gradient(160deg,#f1f2e0,#d6d8bc)"></i></div><p class="name">Product Tittle</p><p class="price">$50.00</p><svg width="16" height="15" viewBox="0 0 16 15"><path d="M8 13.5l-5.8-5.8a3.3 3.3 0 0 1 5.8-3.6a3.3 3.3 0 0 1 5.8 3.6z" fill="none" stroke="#111" stroke-width="1.3"/></svg></article>
    <article class="product" style="left:737px"><div class="thumb"><i role="img" aria-label="Black leather briefcase" style="background:linear-gradient(160deg,#454a53,#1e2026);border-radius:8px"></i></div><p class="name">Product Tittle</p><p class="price">$50.00</p><svg width="16" height="15" viewBox="0 0 16 15"><path d="M8 13.5l-5.8-5.8a3.3 3.3 0 0 1 5.8-3.6a3.3 3.3 0 0 1 5.8 3.6z" fill="none" stroke="#111" stroke-width="1.3"/></svg></article>
    <article class="product" style="left:962px"><div class="thumb"><i role="img" aria-label="Orange weekender duffel bag" style="background:linear-gradient(160deg,#f4a06a,#d9733c);border-radius:26px 26px 14px 14px"></i></div><p class="name">Product Tittle</p><p class="price">$50.00</p><svg width="16" height="15" viewBox="0 0 16 15"><path d="M8 13.5l-5.8-5.8a3.3 3.3 0 0 1 5.8-3.6a3.3 3.3 0 0 1 5.8 3.6z" fill="none" stroke="#111" stroke-width="1.3"/></svg></article>
  </section>

  <section class="collection">
    <h2 class="abs display" style="left:51px;top:1500px;width:221px;text-align:center;font-size:34px">COLLECTION</h2>
    <a class="abs btn-dark" style="left:92px;top:1564px;width:133px;height:41px">SHOP NOW</a>
    <div class="photo" style="left:299px;top:1308px;width:369px;height:496px;background:radial-gradient(ellipse 110px 230px at 185px 300px,rgba(236,230,222,.95),rgba(236,230,222,0) 80%),radial-gradient(circle 42px at 128px 350px,rgba(120,100,88,.75),rgba(120,100,88,0) 90%),linear-gradient(180deg,#d9d4d3,#cbc5c1)" role="img" aria-label="Model in a cream coat and beret with a round brown shoulder bag"></div>
    <div class="photo" style="left:680px;top:1308px;width:369px;height:496px;background:radial-gradient(ellipse 120px 240px at 185px 300px,rgba(238,232,224,.95),rgba(238,232,224,0) 80%),radial-gradient(ellipse 40px 130px at 190px 330px,rgba(226,150,130,.6),rgba(226,150,130,0) 90%),linear-gradient(180deg,#dad5d4,#ccc6c2)" role="img" aria-label="Model in a cream coat over a floral dress with a small blush bag"></div>
    <div class="photo" style="left:1057px;top:1308px;width:143px;height:496px;background:radial-gradient(ellipse 70px 80px at 100px 400px,rgba(248,248,248,.95),rgba(248,248,248,0) 85%),radial-gradient(ellipse 30px 90px at 130px 180px,rgba(190,110,70,.6),rgba(190,110,70,0) 90%),linear-gradient(180deg,#e4e1e0,#d4cfcb)" role="img" aria-label="Model carrying a white tote bag"></div>
  </section>

  <div class="photo" style="left:0;top:1916px;width:1200px;height:614px;background:radial-gradient(ellipse 200px 190px at 640px 400px,rgba(120,85,55,.7),rgba(120,85,55,0) 85%),radial-gradient(ellipse 220px 320px at 560px 330px,rgba(232,222,212,.75),rgba(232,222,212,0) 80%),radial-gradient(ellipse 400px 260px at 200px 580px,rgba(70,80,80,.55),rgba(70,80,80,0) 80%),linear-gradient(100deg,#8a6d5c 0%,#b59a87 35%,#d6c8bc 60%,#b3b1ab 100%)" role="img" aria-label="Woman in sunglasses with a leopard print shoulder bag on a city street"></div>

  <section class="accessories">
    <div class="photo" style="left:51px;top:2643px;width:510px;height:638px;background:radial-gradient(ellipse 170px 280px at 300px 420px,rgba(160,120,90,.8),rgba(160,120,90,0) 80%),radial-gradient(ellipse 90px 60px at 330px 520px,rgba(45,65,55,.8),rgba(45,65,55,0) 90%),linear-gradient(180deg,#a8a7a3 0%,#7b7670 50%,#4d4844 100%)" role="img" aria-label="Woman in a trench coat and beret holding a dark green croc bag"></div>
    <h2 class="abs display" style="left:685px;top:2760px;width:400px;text-align:center;font-size:37px">ACCESSORIES</h2>
    <a class="abs btn-dark" style="left:816px;top:2835px;width:139px;height:43px">SHOP NOW</a>
    <div class="photo" style="left:637px;top:2983px;width:510px;height:298px;background:radial-gradient(ellipse 45px 160px at 285px 150px,rgba(250,250,250,.95),rgba(250,250,250,0) 90%),radial-gradient(ellipse 55px 55px at 350px 160px,rgba(170,95,50,.85),rgba(170,95,50,0) 90%),linear-gradient(180deg,#ead6c0,#dcc3a8)" role="img" aria-label="Woman in white trousers holding a brown leather tote"></div>
    <p class="abs caption" style="left:25px;top:3322px">LOREM IPSUM DOLOR SIT CONSECTETUR</p>
    <p class="abs caption" style="left:611px;top:3322px">LOREM IPSUM DOLOR SIT CONSECTETUR</p>
  </section>

  <section class="abs about">
    <h2 class="display">ABOUT MARGOT LISELLE</h2>
    <p>Lorem ipsum dolor sit amet, consectetur adipiscing elit, sed do eiusmod tempor incididunt ut labore et dolore magna aliqua. Ut enim ad minim veniam, quis nostrud exercitation ullamco laboris nisi ut aliquip ex ea commodo consequat. Duis aute irure dolor in reprehenderit in voluptate velit esse cillum dolore eu fugiat nulla pariatur.</p>
    <a class="abs btn-light">DISCOVER NOW</a>
  </section>
</main>

<footer>
  <div class="abs footer-mark">MARGOT<br>LISELLE</div>
  <h3 class="abs col-head" style="left:340px;top:3943px">COMPANY</h3>
  <ul class="abs col-links" style="left:340px;top:3975px"><li>Home</li><li>About</li><li>Products</li><li>Shop now</li><li>Sign in</li></ul>
  <h3 class="abs col-head" style="left:509px;top:3943px">INFORMATION</h3>
  <ul class="abs col-links" style="left:509px;top:3975px"><li>Terms &amp; Conditions</li><li>Privacy Policy</li><li>Disclaimer</li><li>Site Map</li><li>Categories</li></ul>
  <h3 class="abs col-head" style="left:703px;top:3943px">SUBSCRIBE OUR NEWSLETTER</h3>
  <p class="abs newsletter-note" style="left:703px;top:3979px">Subscribe to our mailing list to receives daily updates direct to your inbox!</p>
  <div class="abs email">Email Address</div>
  <a class="abs btn-dark subscribe">SUBSCRIBE</a>
  <a class="abs social" style="left:699px" aria-label="Email us"><svg width="16" height="12" viewBox="0 0 16 12"><rect x="1" y="1" width="14" height="10" fill="none" stroke="#111" stroke-width="1.4"/><path d="M1 1l7 6 7-6" fill="none" stroke="#111" stroke-width="1.4"/></svg></a>
  <a class="abs social" style="left:742px" aria-label="Call us"><svg width="14" height="14" viewBox="0 0 14 14"><path d="M3 1l2.5 3-1.5 1.5a8 8 0 0 0 4.5 4.5L10 8.5l3 2.5-1.5 2C6 13 1 8 1 2.5z" fill="#111"/></svg></a>
  <a class="abs social" style="left:785px" aria-label="Find our store"><svg width="12" height="16" viewBox="0 0 12 16"><path d="M6 15s5-5.5 5-9A5 5 0 0 0 1 6c0 3.5 5 9 5 9z" fill="#111"/><circle cx="6" cy="6" r="1.8" fill="#fff"/></svg></a>
  <a class="abs social" style="left:827px" aria-label="Shop online"><svg width="14" height="14" viewBox="0 0 14 14"><path d="M2 5h10l-1 8H3z" fill="#111"/><path d="M4.5 5a2.5 2.5 0 0 1 5 0" fill="none" stroke="#111" stroke-width="1.4"/></svg></a>
  <div class="abs rule"></div>
  <p class="abs copyright">Copyrights © margotliselle 2020 &nbsp;|&nbsp; Allrights Reserved</p>
</footer>

</body>
</html>
```